Business card design to suit our website

Need a nice looking business card for our business based off images from our Website and provided images. The business card will require 2 different names (for the 2 owners). The business card should include images from our website, facebook (larkvale coil starter pack) or the pictures provided. it should also contain all contact information.
Our website is www.larkvalecoilworks.com.au
Please dont use image from top bar of website. If images are used please use the ones of our product under the buy it now tab
Updates

Need extra days to review

Target Market(s)

Automotive

Industry/Entity Type

Automotive Part

Contact Information for Business Card

Business Name. contact details including names phone number email. logo
2 business cards needed with 2 different persons names and phone number.

Colors

Designer to choose colors to be used in the design.

Requirements
Must have
• whatever looks best

```html
<!DOCTYPE html>
<html lang="en">
<head>
<meta charset="utf-8">
<title>Larkvale Coil Works business card</title>
<link href="https://fonts.googleapis.com/css2?family=Arimo:wght@400;700&display=swap" rel="stylesheet">
<style>
  :root {
    --stage: #2a2a2c;
    --card-dark: #1d1d1f;
    --card-light: #ffffff;
    --brand-red: #c8192e;
    --text-light: #f2f2f2;
    --silver: #b9bbbe;
    --rule: #6a6a6e;
    --divider: #d4d4d4;
  }
  * { box-sizing: border-box; margin: 0; padding: 0; }
  html, body { width: 1200px; height: 1108px; overflow: hidden; }
  body {
    background: var(--stage);
    font-family: "Arimo", Arial, sans-serif;
    position: relative;
  }
  .card {
    position: absolute;
    top: 209px;
    width: 420px;
    height: 690px;
    border-radius: 26px;
    overflow: hidden;
  }
  .card-front { left: 140px; background: var(--card-dark); }
  .card-back { left: 640px; background: var(--card-light); }

  .brand-name {
    position: absolute;
    font-weight: 700;
    line-height: 1.05;
    text-align: right;
  }
  .card-front .brand-name {
    top: 120px;
    right: 46px;
    font-size: 46px;
    color: var(--brand-red);
  }
  .brand-name span { display: block; font-size: 0.56em; }

  .person {
    position: absolute;
    top: 392px;
    right: 46px;
    width: 280px;
    text-align: right;
  }
  .person-name {
    color: var(--brand-red);
    font-weight: 700;
    font-size: 22px;
    letter-spacing: 0.5px;
  }
  .person-title {
    color: var(--text-light);
    font-size: 17px;
    margin-top: 4px;
  }
  .person-rule {
    border: 0;
    border-top: 1px solid var(--rule);
    margin: 16px 0 0 40px;
  }
  .contact {
    position: absolute;
    top: 494px;
    right: 46px;
    list-style: none;
    text-align: right;
    color: var(--text-light);
    font-size: 17px;
    line-height: 1.45;
  }
  .contact b { color: var(--brand-red); font-weight: 400; margin-right: 6px; }

  .photo-row {
    position: absolute;
    left: 0;
    width: 100%;
    display: flex;
    align-items: center;
    justify-content: space-between;
    padding: 0 24px;
  }
  .photo-row.top { top: 0; height: 256px; }
  .photo-row.bottom { top: 408px; height: 282px; }
  .photo {
    width: 168px;
    border-radius: 6px;
  }
  .photo-row.top .photo { height: 190px; }
  .photo-row.bottom .photo { height: 210px; }
  .photo.kit-box { background: linear-gradient(160deg, #e8e8ea, #b8202f 55%, #8e1a26); }
  .photo.parts { background: linear-gradient(160deg, #f4f4f5, #c9cbce 60%, #5a5a5e); }
  .photo-divider {
    width: 1px;
    align-self: stretch;
    margin: 36px 0;
    background: var(--divider);
  }
  .brand-band {
    position: absolute;
    top: 256px;
    left: 0;
    width: 100%;
    height: 152px;
    background: var(--card-dark);
  }
  .brand-band .brand-name {
    top: 34px;
    right: 46px;
    font-size: 44px;
    color: var(--silver);
  }
</style>
</head>
<body>
  <section class="card card-front">
    <div class="brand-name">Larkvale<span>Coil Works</span></div>
    <div class="person">
      <div class="person-name">MARCUS HALE</div>
      <div class="person-title">Managing Director</div>
      <hr class="person-rule">
    </div>
    <ul class="contact">
      <li><b>P:</b>1300 482 170</li>
      <li><b>M:</b>0412 555 308</li>
      <li><b>E:</b>sales@larkvalecoilworks.com.au</li>
      <li><b>W:</b>www.larkvalecoilworks.com.au</li>
    </ul>
  </section>

  <section class="card card-back">
    <div class="photo-row top">
      <div class="photo kit-box" role="img" aria-label="Boxed coil starter pack with instruction sheet"></div>
      <div class="photo-divider"></div>
      <div class="photo parts" role="img" aria-label="Switch housing, bolts and bracket parts"></div>
    </div>
    <div class="brand-band">
      <div class="brand-name">Larkvale<span>Coil Works</span></div>
    </div>
    <div class="photo-row bottom">
      <div class="photo parts" role="img" aria-label="Five-barrel parts set with bracket and key blank"></div>
      <div class="photo-divider"></div>
      <div class="photo parts" role="img" aria-label="Ten-barrel parts set with bracket and key blank"></div>
    </div>
  </section>
</body>
</html>
```